A nerdy designer needs an artistic designer!

Quillfen Apparatus is an applied research/engineering company - we turn a desired product/capability into something tangible through the application of mathematics, physics, electronics and software engineering. We have a few products of our own, but we also offer contract design services. As a designer, you'd be familiar with our problem - how do you convey what you do when you can do anything a client asks?
Updates

Good evening, Thankyou to all of the designers who have messaged me asking if they can only do the design work (and have someone else perform the site coding) but I don't know how to partition the job into two - i.e. 1. design, 2. coding. The makerhive site only gave me the options of: 1. web design, or 2. web design + coding (+$150). I chose option #2, because this is what I ultimately need - a functional website. I'll escalate it to the makerhive helpdesk and ask, but I suspect their answer will be "No. The designer must do both." I sympathise, because there are some things I do well, and some things I don't do at all (like websites). I'll let you know what I learn. Cheers, J

Target Market(s)

Our audience is predominantly technical, so we'd like to have a site which is easy to navigate and find relevant information without too many visually distracting 'popups'/sliding panes etc.

We've provided a series of photos of past projects/examples, all of which:

a. we own,
b. can be cropped/edited/artistically hacked at will etc

to watermark/pepper the pages with to convey a sense of realism/credibility. They're they're as representative images only and not mandatory. Feel free to use them or ignore them as you wish.

Coding

Coded - Design and coding required

Number of Pages Required

5+ page

Font styles to use
Serif
Sans Serif

Colors

Designer to choose colors to be used in the design.

Requirements
Must have
• Editable text. (i.e. nothing permanently embedded in the graphics as the page(s) are likely to evolve fairly rapidly)
Nice to have
• We're pretty open to ideas. Your artistic eye(s) will far exceed anything us (stereotypically) nerdy folk could suggest!

```html
<!DOCTYPE html>
<html lang="en">
<head>
<meta charset="utf-8">
<title>Quillfen Apparatus</title>
<link href="https://fonts.googleapis.com/css2?family=Mulish:wght@400;600;700;800&family=Raleway:wght@400;500&display=swap" rel="stylesheet">
<style>
:root{
  --orange:#f7680f;
  --ink:#2b2b2b;
  --body:#4a4a4a;
  --muted:#5c5c5c;
  --grey-band:#efefef;
  --footer:#1b1b1b;
  --white:#ffffff;
  --line:#bdbdbd;
}
*{margin:0;padding:0;box-sizing:border-box}
html,body{width:1200px;height:3197px;overflow:hidden;background:var(--white)}
body{position:relative;font-family:"Mulish",sans-serif;color:var(--ink)}
.abs{position:absolute}
.top-rule{left:0;top:0;width:1200px;height:4px;background:var(--orange)}
.site-header{left:0;top:4px;width:1200px;height:120px;background:var(--white);border-bottom:1px solid #e4e4e4}
.brand{left:112px;top:34px;display:flex;align-items:center;gap:10px}
.brand-dot{width:44px;height:44px;border-radius:50%;background:var(--ink)}
.brand-name{font-family:"Mulish",sans-serif;font-weight:800;font-size:22px;line-height:1.05;color:var(--ink);letter-spacing:1px;text-transform:uppercase}
.main-nav{top:58px;font-size:13.5px;font-weight:600;text-transform:uppercase;color:var(--ink)}
.main-nav.active{color:var(--orange)}
.hero{left:0;top:124px;width:1200px;height:668px;background:linear-gradient(100deg,#b7b9bb 0%,#9ea3a8 25%,#5a6f93 45%,#2f4f8c 62%,#3c5fa0 80%,#2a3f6b 100%)}
.hero-title{left:696px;top:352px;font-size:40px;font-weight:600;color:var(--white)}
.hero-text{left:697px;top:422px;width:420px;font-size:17px;line-height:35px;color:var(--white)}
.btn{display:flex;align-items:center;justify-content:center;background:var(--orange);color:var(--white);font-size:17px;border-radius:2px}
.dot{top:760px;width:11px;height:11px;border-radius:50%;background:var(--white)}
.dot.on{background:var(--orange)}
.about-lead{left:112px;top:868px;font-size:31px;font-weight:600;color:var(--ink)}
.about-title{left:112px;top:910px;font-size:35px;font-weight:600;color:var(--orange)}
.para{font-family:"Raleway",sans-serif;font-size:13.4px;line-height:25.7px;color:var(--body);text-align:justify}
.about-photo{left:655px;top:854px;width:396px;height:396px;border-radius:50%;background:radial-gradient(circle at 50% 40%,#c98a52 0%,#6b3d55 35%,#2c3a5e 70%,#1e2540 100%)}
.featured{left:0;top:1351px;width:1200px;height:622px;background:var(--grey-band)}
.section-title{width:1200px;left:0;text-align:center;font-size:32px;font-weight:600;color:var(--ink)}
.underline{left:568px;width:64px;height:3px;background:var(--orange)}
.equip-photo{top:1501px;width:249px;height:249px;border-radius:50%}
.equip-name{top:1768px;width:330px;text-align:center;font-size:24px;font-weight:600;color:var(--ink)}
.equip-text{top:1815px;width:330px;text-align:center;font-family:"Raleway",sans-serif;font-size:12.6px;line-height:26px;color:var(--muted)}
.applied{left:0;top:1973px;width:1200px;height:487px;background:linear-gradient(90deg,#ececec 0%,#e9e9e9 45%,#dcdcdc 55%,#c8c9cc 65%,#9fa2a8 78%,#7c8088 90%,#b9bcc2 100%)}
.applied-lead{left:111px;top:2050px;font-size:28px;font-weight:600;color:var(--ink)}
.applied-title{left:111px;top:2094px;font-size:30px;font-weight:600;color:var(--ink)}
.applied-title span{color:var(--orange)}
.newsletter-text{left:230px;top:2582px;width:740px;text-align:center;font-family:"Raleway",sans-serif;font-size:13.4px;line-height:26px;color:var(--muted)}
.email-field{left:231px;top:2677px;width:737px;height:51px;border:1px solid var(--line);border-radius:3px;padding-left:18px;display:flex;align-items:center;font-family:"Raleway",sans-serif;font-size:13.4px;color:var(--muted)}
.subscribe{left:521px;top:2751px;width:158px;height:46px;font-size:15px;font-weight:600;text-transform:uppercase}
.site-footer{left:0;top:2855px;width:1200px;height:342px;background:var(--footer)}
.footer-brand{left:150px;top:2940px;width:222px;text-align:center}
.footer-brand .brand-dot{width:96px;height:96px;margin:0 auto 18px;background:var(--white)}
.footer-brand .brand-name{color:var(--white);font-size:30px;letter-spacing:2px}
.footer-head{top:2890px;font-size:17px;font-weight:600;color:var(--white);text-transform:uppercase}
.footer-list{list-style:none;font-size:14px;color:var(--white)}
.footer-list li{height:30px;display:flex;align-items:center}
.footer-list li::before{content:"»";width:30px;padding-left:4px}
.footer-note{left:875px;top:2931px;width:200px;font-size:13px;line-height:25px;color:var(--white)}
.social{top:3001px;width:31px;height:31px;border-radius:50%;border:1.5px solid var(--white)}
.footer-rule{left:112px;top:3125px;width:976px;height:1px;background:#3a3a3a}
.copyright{left:0;top:3154px;width:1200px;text-align:center;font-size:13px;color:var(--white)}
</style>
</head>
<body>
<div class="abs top-rule"></div>

<header class="abs site-header"></header>
<div class="abs brand"><span class="brand-dot"></span><span class="brand-name">Quillfen<br>Apparatus</span></div>
<nav>
  <span class="abs main-nav active" style="left:461px">Home</span>
  <span class="abs main-nav" style="left:555px">About Us</span>
  <span class="abs main-nav" style="left:677px">Services</span>
  <span class="abs main-nav" style="left:794px">Features</span>
  <span class="abs main-nav" style="left:916px">Blog</span>
  <span class="abs main-nav" style="left:1006px">Contact Us</span>
</nav>

<section class="abs hero" role="img" aria-label="Scientist's hand adjusting a steel probe on a blue laboratory instrument"></section>
<h1 class="abs hero-title">Quillfen Apparatus</h1>
<p class="abs hero-text">Sed ut perspiciatis unde omnis iste natus error sit voluptatem accusantium doloremque</p>
<a class="abs btn" style="left:699px;top:525px;width:132px;height:49px">Read More</a>
<span class="abs dot" style="left:577px"></span>
<span class="abs dot on" style="left:595px"></span>
<span class="abs dot" style="left:613px"></span>

<h2 class="abs about-lead">About Our</h2>
<h2 class="abs about-title">Quillfen Apparatus</h2>
<p class="abs para" style="left:112px;top:982px;width:457px">Sed ut perspiciatis unde omnis iste natus error sit voluptatem accusantium doloremque laudantium, totam rem aperiam, eaque ipsa quae ab illo inventore veritatis et quasi architecto beatae vitae dicta sunt explicabo. Nemo enim ipsam voluptatem quia voluptas sit aspernatur aut odit aut fugit, sed quia consequuntur magni dolores eos qui ratione voluptatem sequi nesciunt. Neq ue porro quisquam est, qui dolorem ipsum quia dolor sit amet, consectetur, adipisci velit, sed quia non numquam eius modi tempora.Ut enim ad minima cipit laboriosam, nisi ut aliquid ex ea commodi consequatur</p>
<a class="abs btn" style="left:112px;top:1225px;width:138px;height:49px">Read More</a>
<div class="abs about-photo" role="img" aria-label="Circuit board under a microscope in a lab"></div>

<section class="abs featured"></section>
<h2 class="abs section-title" style="top:1389px">Featured Equipment</h2>
<div class="abs underline" style="top:1445px"></div>
<div class="abs equip-photo" style="left:125px;background:radial-gradient(circle at 60% 30%,#6d9bc9,#2d4e77 55%,#b7c3cf 100%)" role="img" aria-label="Oscilloscope and probe testing a circuit"></div>
<div class="abs equip-photo" style="left:474px;background:radial-gradient(circle at 50% 65%,#c48a40,#5a3a5a 45%,#2c3654 100%)" role="img" aria-label="Microscope over an illuminated circuit board"></div>
<div class="abs equip-photo" style="left:823px;background:radial-gradient(circle at 50% 60%,#f3f3f3,#d6d9de 50%,#8b97a8 100%)" role="img" aria-label="Gloved hand pipetting into a white benchtop analyser"></div>
<h3 class="abs equip-name" style="left:85px">Equipment 01</h3>
<h3 class="abs equip-name" style="left:434px">Equipment 02</h3>
<h3 class="abs equip-name" style="left:783px">Equipment 03</h3>
<p class="abs equip-text" style="left:85px">Sed ut perspiciatis unde omnis iste natus error<br>sit voluptatem accusantium doloremque laudan<br>beatae vitae dicta sunt explicabo.</p>
<p class="abs equip-text" style="left:434px">Sed ut perspiciatis unde omnis iste natus error<br>sit voluptatem accusantium doloremque laudan<br>beatae vitae dicta sunt explicabo.</p>
<p class="abs equip-text" style="left:783px">Sed ut perspiciatis unde omnis iste natus error<br>sit voluptatem accusantium doloremque laudan<br>beatae vitae dicta sunt explicabo.</p>

<section class="abs applied" role="img" aria-label="White and black laboratory analyser with blue tubing, fading into a light grey backdrop"></section>
<h2 class="abs applied-lead">Quillfen Apparatus is an</h2>
<h2 class="abs applied-title"><span>applied research/engineering</span> company</h2>
<p class="abs para" style="left:111px;top:2161px;width:485px">Sed ut perspiciatis unde omnis iste natus error sit voluptatem accusantium dolo rem que laudantium, totam rem aperiam, eaque ipsa quae ab illo inventore veritatis et quasi architecto beatae vitae dicta sunt explicabo. Nemo enim ipsam volupt atem quia volu ptas sit aspernatur aut odit aut fugit, sed quia consequuntur magni dolores eos qui ratione voluptatem sequi nesciunt.</p>
<a class="abs btn" style="left:112px;top:2327px;width:138px;height:48px;font-size:18px">Read More</a>

<h2 class="abs section-title" style="top:2506px;font-size:33px">Our Newsletter Signup</h2>
<div class="abs underline" style="top:2562px"></div>
<p class="abs newsletter-text">Sed ut perspiciatis unde omnis iste natus error sit voluptatem accusantium doloremque laudantium, totam rem aperiam, illo inventore veritatis et quasi architecto beatae vitae dicta sunt explicabo.</p>
<div class="abs email-field">Enter Your Email Id :</div>
<a class="abs btn subscribe">Subscribe</a>

<footer class="abs site-footer"></footer>
<div class="abs footer-brand"><div class="brand-dot"></div><div class="brand-name">Quillfen<br>Apparatus</div></div>
<h4 class="abs footer-head" style="left:453px">Quick Links</h4>
<ul class="abs footer-list" style="left:453px;top:2927px">
  <li>Home</li><li>About Us</li><li>Services</li><li>Features</li><li>Blog</li><li>Contact Us</li>
</ul>
<h4 class="abs footer-head" style="left:643px">Products</h4>
<ul class="abs footer-list" style="left:643px;top:2927px">
  <li>Sed ut perspiciatis</li><li>unde omnis iste</li><li>natus error sit</li><li>voluptatem</li><li>accusantium</li>
</ul>
<h4 class="abs footer-head" style="left:875px">Follow Us</h4>
<p class="abs footer-note">Sed ut perspiciatis unde omnis natus error sit voluptatem</p>
<span class="abs social" style="left:875px" aria-label="Social link"></span>
<span class="abs social" style="left:911px" aria-label="Social link"></span>
<span class="abs social" style="left:947px" aria-label="Social link"></span>
<span class="abs social" style="left:983px" aria-label="Social link"></span>
<span class="abs social" style="left:1019px" aria-label="Social link"></span>
<div class="abs footer-rule"></div>
<p class="abs copyright">© Copyright 2019 Quillfen Apparatus.All Rights Reserved</p>
</body>
</html>
```